Frame Glow Entertainment | Business Card & Logo

We are looking for a business card with a Logo.
It’s a brand new business and we are looking for an elegant design.
The business service categories are:
Photo Booth
Photography
Events Planning
Marcus Pellham
0471926358
0381736492
info@frameglowentertainment.com.au
www.frameglowentertainment.com.au
Target Market(s)
Corporate, Photo Booth, Photography and event planning
Industry/Entity Type
Photo Booth, Photography and event planning
Contact Information for Business Card
Marcus Pellham | 0471926358 | 0381736492 | info@frameglowentertainment.com.au | www.frameglowentertainment.com.au

```html
<!DOCTYPE html>
<html lang="en">
<head>
<meta charset="utf-8">
<title>Frame Glow Entertainment – Business Card</title>
<link href="https://fonts.googleapis.com/css2?family=Montserrat:wght@400;500&display=swap" rel="stylesheet">
<style>
  :root {
    --stage: #e4e3e1;
    --card: #0b0b0b;
    --gold: #c9a24a;
    --gold-dark: #8a6a22;
    --gold-light: #f0d78a;
    --text-light: #f2f2f2;
    --text-muted: #cfcfcf;
  }
  * { box-sizing: border-box; margin: 0; padding: 0; }
  html, body {
    width: 1200px; height: 1199px; overflow: hidden;
    background: var(--stage);
    font-family: "Montserrat", sans-serif;
  }
  .canvas {
    width: 1200px; height: 1199px;
    display: flex; flex-direction: column; align-items: center; justify-content: center;
    gap: 60px;
  }
  .card {
    position: relative;
    width: 820px; height: 500px;
    background: var(--card);
    overflow: hidden;
    box-shadow: 0 10px 30px rgba(0,0,0,0.18);
  }
  .card__band {
    position: absolute; left: 0; right: 0; bottom: 0; height: 14px;
    background: linear-gradient(90deg, var(--gold-dark), var(--gold-light) 35%, var(--gold) 60%, var(--gold-light) 85%, var(--gold-dark));
  }
  .brand-name {
    color: var(--gold);
    font-family: "Montserrat", sans-serif;
    font-weight: 400;
    text-transform: uppercase;
    letter-spacing: 0.12em;
    white-space: nowrap;
  }

  /* Contact side */
  .card--contact .brand-name {
    position: absolute; left: 60px; top: 120px;
    font-size: 27px;
  }
  .contact__leader {
    position: absolute; left: 60px; top: 232px; width: 420px;
    border-top: 2px dotted var(--gold);
  }
  .contact__name {
    position: absolute; right: 60px; top: 214px;
    color: var(--text-light);
    font-size: 28px; font-weight: 500;
  }
  .contact__phones {
    position: absolute; right: 60px; top: 266px;
    list-style: none;
    color: var(--text-light); font-size: 16px;
  }
  .contact__phones li,
  .contact__online li {
    display: flex; align-items: center; justify-content: flex-end; gap: 10px;
    line-height: 26px;
  }
  .contact__online {
    position: absolute; right: 60px; top: 390px;
    list-style: none;
    color: var(--text-light); font-size: 16px;
  }
  .icon { width: 14px; height: 14px; flex: none; }

  /* Brand side */
  .card--brand .brand-name {
    position: absolute; left: 0; right: 0; top: 200px;
    text-align: center;
    font-size: 36px;
  }
  .services {
    position: absolute; left: 0; right: 0; top: 300px;
    display: flex; justify-content: center; gap: 22px;
    color: var(--text-muted); font-size: 19px; letter-spacing: 0.02em;
  }
  .services__divider { color: var(--text-muted); }
</style>
</head>
<body>
<main class="canvas">

  <section class="card card--contact" aria-label="Business card contact side">
    <p class="brand-name">Frame Glow Entertainment</p>
    <div class="contact__leader"></div>
    <h1 class="contact__name">Marcus Pellham</h1>
    <ul class="contact__phones">
      <li>0471926358
        <svg class="icon" viewBox="0 0 16 16" fill="none" stroke="#f2f2f2" stroke-width="1.3"><path d="M3.5 1.5l2.5 3-1.5 1.5c.8 2 2.5 3.7 4.5 4.5L10.5 9l3 2.5-1.5 2.5C7 14 2 9 2 3z"/></svg>
      </li>
      <li>0381736492
        <svg class="icon" viewBox="0 0 16 16" fill="none" stroke="#f2f2f2" stroke-width="1.3"><path d="M3.5 1.5l2.5 3-1.5 1.5c.8 2 2.5 3.7 4.5 4.5L10.5 9l3 2.5-1.5 2.5C7 14 2 9 2 3z"/></svg>
      </li>
    </ul>
    <ul class="contact__online">
      <li>info@frameglowentertainment.com.au
        <svg class="icon" viewBox="0 0 16 16" fill="none" stroke="#f2f2f2" stroke-width="1.3"><rect x="1.5" y="3.5" width="13" height="9"/><path d="M1.5 3.5l6.5 5 6.5-5"/></svg>
      </li>
      <li>www.frameglowentertainment.com.au
        <svg class="icon" viewBox="0 0 16 16" fill="none" stroke="#f2f2f2" stroke-width="1.2"><circle cx="8" cy="8" r="6.5"/><ellipse cx="8" cy="8" rx="3" ry="6.5"/><path d="M1.5 8h13"/></svg>
      </li>
    </ul>
    <div class="card__band"></div>
  </section>

  <section class="card card--brand" aria-label="Business card brand side">
    <p class="brand-name">Frame Glow Entertainment</p>
    <p class="services">
      <span>Photo Booth</span><span class="services__divider">|</span>
      <span>Photography</span><span class="services__divider">|</span>
      <span>Events Planning</span>
    </p>
    <div class="card__band"></div>
  </section>

</main>
</body>
</html>
```